Tick Tock Green Frog

I'm looking for one generic business card that be used for four people or would it be easier to get four different design of cards.

I have attached the logo, of the cow. I would also like to use one colour of the cow's legs in the background.

Info for card:
Dana Whitcombe
Wrangler of Opportunities
Phone: 047 218 5904
email: dana.whitcombe@ticktockgreenfrogs.com.au
Web: www.ticktockgreenfrogs.com.au

Here is some tag lines that could also be used:

"Moo-ving you in the right direction"

"Putting the Tick Tock back into early childhood"
"Where's there is NO bull"

```html
<!DOCTYPE html>
<html lang="en">
<head>
<meta charset="utf-8">
<title>Tick Tock Green Frog – Business Cards</title>
<link href="https://fonts.googleapis.com/css2?family=Arimo:wght@400;700&family=Archivo+Narrow:wght@400&display=swap" rel="stylesheet">
<style>
  :root {
    --backdrop: #e4e5e7;
    --card-orange: #f4620a;
    --card-white: #ffffff;
    --brown-dark: #3f2410;
    --brown-mid: #5a3414;
    --leg-green: #1c6b14;
    --leaf-green: #6aa51e;
    --accent-orange: #f08a12;
    --text-grey: #555555;
    --text-white: #ffffff;
  }
  * { margin: 0; padding: 0; box-sizing: border-box; }
  html, body { width: 1200px; height: 800px; overflow: hidden; }
  body {
    background: var(--backdrop);
    font-family: "Arimo", Arial, sans-serif;
    position: relative;
  }
  .card {
    position: absolute;
    top: 241px;
    width: 520px;
    height: 318px;
    overflow: hidden;
    box-shadow: 0 6px 18px rgba(0,0,0,0.12);
  }
  .wordmark__name {
    font-weight: 700;
    font-size: 20px;
    line-height: 1.1;
    color: var(--brown-dark);
    white-space: nowrap;
  }
  .wordmark__sub {
    margin-top: 3px;
    font-size: 11px;
    color: var(--brown-dark);
    white-space: nowrap;
  }

  /* Front side */
  .card--front { left: 40px; background: var(--card-orange); }
  .card--front .illustration {
    position: absolute;
    left: 0; top: 0;
    width: 250px; height: 225px;
    border-radius: 0 0 36px 0;
    background: linear-gradient(160deg, var(--brown-dark) 0%, var(--brown-mid) 70%, var(--leg-green) 100%);
  }
  .card--front .wordmark {
    position: absolute;
    left: 266px; top: 150px;
  }
  .card--front .tagline {
    position: absolute;
    left: 150px; top: 252px;
    font-size: 16px;
    color: var(--text-white);
    white-space: nowrap;
  }
  .tagline strong { font-weight: 700; text-transform: uppercase; }

  /* Back side */
  .card--back { left: 640px; background: var(--card-white); }
  .card--back .illustration {
    position: absolute;
    left: 28px; top: 24px;
    width: 250px; height: 140px;
    border-radius: 32px;
    background: linear-gradient(160deg, var(--brown-dark) 0%, var(--brown-mid) 75%, var(--leaf-green) 100%);
  }
  .card--back .wordmark {
    position: absolute;
    left: 28px; top: 176px;
  }
  .card--back .wordmark__sub { color: var(--accent-orange); font-weight: 700; }

  .contact {
    position: absolute;
    left: 290px; top: 200px;
    width: 220px;
  }
  .contact__name {
    font-weight: 700;
    font-size: 15px;
    color: var(--accent-orange);
  }
  .contact__role {
    font-family: "Archivo Narrow", "Arial Narrow", sans-serif;
    font-size: 12px;
    color: var(--text-grey);
    margin: 2px 0 8px;
  }
  .contact__list { list-style: none; }
  .contact__item {
    display: flex;
    align-items: center;
    gap: 6px;
    font-family: "Archivo Narrow", "Arial Narrow", sans-serif;
    font-size: 11px;
    line-height: 16px;
    color: var(--text-grey);
    white-space: nowrap;
  }
  .contact__icon { width: 10px; height: 10px; flex: none; }
</style>
</head>
<body>

  <section class="card card--front">
    <div class="illustration" role="img" aria-label="Brand mascot illustration in brown with green legs"></div>
    <div class="wordmark">
      <p class="wordmark__name">Tick Tock Green Frog</p>
      <p class="wordmark__sub">creative consulting for early childhood</p>
    </div>
    <p class="tagline">Putting the <strong>Tick Tock</strong> into early childhood</p>
  </section>

  <section class="card card--back">
    <div class="illustration" role="img" aria-label="Brand mascot illustration in brown with colourful legs and tail"></div>
    <div class="wordmark">
      <p class="wordmark__name">Tick Tock Green Frog</p>
      <p class="wordmark__sub">creative consulting for early childhood</p>
    </div>
    <div class="contact">
      <p class="contact__name">Dana Whitcombe</p>
      <p class="contact__role">Wrangler of Opportunities</p>
      <ul class="contact__list">
        <li class="contact__item">
          <svg class="contact__icon" viewBox="0 0 10 10"><rect x="2" y="0.5" width="6" height="9" rx="1.2" fill="#6aa51e"/><rect x="3" y="1.8" width="4" height="5" fill="#fff"/></svg>
          047 218 5904
        </li>
        <li class="contact__item">
          <svg class="contact__icon" viewBox="0 0 10 10"><rect x="0.5" y="2" width="9" height="6" rx="1" fill="#6aa51e"/><path d="M1 2.5 L5 5.5 L9 2.5" stroke="#fff" stroke-width="1" fill="none"/></svg>
          dana.whitcombe@ticktockgreenfrogs.com.au
        </li>
        <li class="contact__item">
          <svg class="contact__icon" viewBox="0 0 10 10"><circle cx="5" cy="5" r="4.5" fill="#6aa51e"/><path d="M0.5 5 H9.5 M5 0.5 C2.5 3 2.5 7 5 9.5 M5 0.5 C7.5 3 7.5 7 5 9.5" stroke="#fff" stroke-width="0.8" fill="none"/></svg>
          www.ticktockgreenfrogs.com.au
        </li>
      </ul>
    </div>
  </section>

</body>
</html>
```